Homepage for experience sharing site- interesting, fun and personable!

We need a homepage design for an experience sharing website. The tag line is 'find, promote and share great times!' The homepage should be exciting and innovative and illustrate the values of the site: possibility, freedom and life. It should be fun and personable.

To give you a clearer example, here are a few of the 'great times' users will be sharing on the site:

Club night, warehouse rave or beach gig
Antarctic expedition, Cambodian jungle trek
Cooking and surfing classes
Sumo speed dating
Drag racing and quad biking
Birthday parties, pub crawls and comedy nights

We like the idea of some sort of map or background image from which a few experiences pop up; however we are open to other ideas. The links below should give you an idea of the concept.

http://www.korvane.com/harbor#/harbor-story
http://www.pimbleo.com/map/
http://www.vidquarra.com/watch?v=QT7KWLR2zpa
Updates

Hi,

please do not feel that your design must include a map, that was just an idea. If you can produce a design that delivers the message immediately and gets the user interested without a map then that is great! 

Please do not feel constrained.

Thanks,

Marisol

Hi,

I've created and attached two examples to the brief, which I hope will provide some guidance. I want the homepage design to concentrate on the human element and the concept of creating and sharing experiences.

Thanks,

Marisol  

Target Market(s)

18-37 age range. People who enjoy life and new experiences.

Industry/Entity Type

Racing

Requirements
Must have
• It must communicate the human element of the site... please see the attached examples I made as guidance

It must deliver the message as simply as possible

Could you ensure that your design includes the following elements please:

* breadcrumbs
* a search box
* the login and register should be part of the header block
Should not have
• Unnecessary elements

Only yellow

```html
<!DOCTYPE html>
<html lang="en">
<head>
<meta charset="utf-8">
<title>GOODDAYSOUT.NET – Promote Great Times</title>
<link rel="stylesheet" href="https://fonts.googleapis.com/css2?family=Oswald:wght@400;500;700&family=Roboto+Condensed:wght@400;700&display=swap">
<style>
:root{
  --yellow:#ffe600;
  --yellow-soft:#fff35a;
  --orange:#ffb400;
  --red:#e60012;
  --dark:#140d07;
  --wood:#4a3220;
  --wood-dark:#1e140b;
  --teal:#5fb8a8;
  --teal-dark:#2d7066;
  --white:#ffffff;
  --ink:#111111;
}
*{box-sizing:border-box;margin:0;padding:0}
html,body{width:1200px;height:960px;overflow:hidden}
body{position:relative;font-family:"Roboto Condensed",sans-serif;color:var(--white);
  background:radial-gradient(ellipse at 50% 40%,#6b4a2e 0%,var(--wood) 30%,var(--wood-dark) 65%,#080503 100%)}
.site-header{position:absolute;left:0;top:0;width:1200px;height:144px;
  background:radial-gradient(ellipse at 15% 10%,#ff7a00 0%,#ffb800 18%,var(--yellow) 45%,var(--yellow-soft) 100%)}
.brand{position:absolute;left:150px;top:40px}
.brand-name{font-family:"Oswald",sans-serif;font-weight:700;font-size:40px;line-height:1;color:var(--ink);letter-spacing:-1px}
.tagline{font-family:"Oswald",sans-serif;font-size:19px;color:var(--ink);margin-top:8px;letter-spacing:.2px}
.search{position:absolute;left:725px;top:44px;width:280px;height:26px;border-radius:5px;background:#fffbe6;border:2px solid #c99a3a;font-size:12px;color:#222;padding:4px 10px}
.search-btn{position:absolute;left:1016px;top:44px;width:30px;height:28px;border-radius:5px;background:var(--red)}
.select{position:absolute;top:92px;width:124px;height:20px;background:#fffbe6;border:1px solid #c99a3a;border-radius:3px;font-size:12px;color:#222;padding:2px 8px}
.select::after{content:"";position:absolute;right:0;top:0;width:26px;height:18px;background:var(--red)}
.select-country{left:725px}.select-price{left:860px}
.filter-btn{position:absolute;left:998px;top:93px;width:47px;height:19px;background:var(--red);color:#fff;font-size:13px;text-align:center;line-height:19px;border-radius:2px}
.main-nav{position:absolute;left:155px;top:146px;width:890px;height:40px;border-radius:0 0 8px 8px;
  background:linear-gradient(#8fd6c8,var(--teal) 50%,var(--teal-dark));display:flex;align-items:center}
.main-nav a{font-family:"Oswald",sans-serif;font-size:20px;color:#fff;text-decoration:none;text-align:center;height:40px;line-height:40px;border-right:1px solid rgba(0,0,0,.25)}
.main-nav a.active{color:var(--yellow)}
.nav-pointer{position:absolute;left:500px;top:188px}
.breadcrumb{position:absolute;left:156px;top:232px;font-family:"Oswald",sans-serif;font-size:16px}
.breadcrumb a{color:#fff;text-decoration:underline}.breadcrumb .current{color:var(--yellow)}
.sub-nav{position:absolute;left:600px;top:232px;width:445px;height:36px;border-radius:8px 8px 0 0;background:linear-gradient(#ffe14a,var(--orange));
  display:flex;gap:16px;align-items:center;justify-content:center;font-family:"Oswald",sans-serif;font-size:13px;color:var(--ink)}
.sub-nav .active{color:#e65a00}
.hero{position:absolute;left:155px;top:268px;width:890px;height:327px;background:linear-gradient(180deg,#d9dde0 0%,#9fa8ae 45%,#3b3a38 75%,#141210 100%)}
.hero-arrows{position:absolute;left:16px;top:16px}
.hero-title{position:absolute;right:22px;top:158px;text-align:right;font-family:"Oswald",sans-serif;font-weight:700;line-height:.9}
.hero-title .big{font-size:84px;color:var(--orange)}.hero-title .side{font-size:46px;color:var(--red)}
.hero-title .sub{display:block;font-size:36px;color:var(--yellow);font-weight:500}
.hero-caption{position:absolute;right:22px;top:278px;width:820px;text-align:right;font-size:13px;line-height:17px}
.hero-down{position:absolute;right:20px;top:116px}
.thumbs{position:absolute;left:155px;top:608px;display:flex;gap:12px}
.thumb{width:118px;height:77px;border:3px solid var(--red)}
.thumb.active{border-color:var(--yellow)}
.thumb.band{background:linear-gradient(#cfd3d6,#4a4843)}
.thumb.rock{background:linear-gradient(#e4e2de,#6f6a60)}
.thumb.forest{background:linear-gradient(#2c6b64,#0e1f1c)}
.intro{position:absolute;left:156px;top:712px;width:540px}
.intro h1{font-family:"Oswald",sans-serif;font-weight:500;font-size:32px;color:var(--yellow)}
.intro h1 span{color:var(--red)}
.intro p{font-size:13px;line-height:17px;margin-top:8px}
.promote-btn{position:absolute;left:820px;top:722px;width:215px;height:62px;border-radius:14px;background:linear-gradient(var(--yellow-soft),var(--orange));
  font-family:"Oswald",sans-serif;font-weight:700;font-size:38px;line-height:62px;text-align:center;color:#c23a00}
.social{position:absolute;left:820px;top:812px;display:flex;gap:14px}
.social span{width:46px;height:46px;border-radius:50%;display:block}
.social .rss{background:#f08a24}.social .s2{background:#2f5fa6}.social .s3{background:#47b3e3}.social .s4{background:#f2f2f2}
.site-footer{position:absolute;left:0;top:890px;width:1200px;height:70px;background:linear-gradient(90deg,var(--yellow),var(--yellow-soft) 60%,#f5d400)}
.footer-nav{position:absolute;left:155px;top:22px;font-family:"Oswald",sans-serif;font-size:16px;color:var(--ink)}
.footer-nav .active{color:var(--red)}
.footer-legal{position:absolute;right:155px;top:26px;text-align:right;font-size:10px;color:var(--ink);line-height:14px}
.footer-legal small{color:#6b5a00;font-size:9px}
</style>
</head>
<body>
<header class="site-header">
  <div class="brand">
    <div class="brand-name">GOODDAYSOUT.NET</div>
    <div class="tagline">FIND • PROMOTE • SHARE GREAT TIMES</div>
  </div>
  <div class="search">Search...</div>
  <div class="search-btn"><svg width="30" height="28"><circle cx="14" cy="13" r="6" fill="none" stroke="#fff" stroke-width="2"/><line x1="18" y1="17" x2="23" y2="22" stroke="#fff" stroke-width="2.5"/></svg></div>
  <div class="select select-country">Country...</div>
  <div class="select select-price">Price...</div>
  <div class="filter-btn">Filter</div>
</header>

<nav class="main-nav">
  <a href="#" style="width:60px"><svg width="20" height="18" viewBox="0 0 20 18"><path d="M10 1 L19 9 H16 V17 H12 V12 H8 V17 H4 V9 H1Z" fill="#fff"/></svg></a>
  <a href="#" style="width:190px">Find Great Times</a>
  <a href="#" class="active" style="width:210px">Promote Great Times</a>
  <a href="#" style="width:225px">Share Great Times</a>
  <a href="#" style="width:115px">Register</a>
  <a href="#" style="width:90px;border-right:0">Login</a>
</nav>
<svg class="nav-pointer" width="26" height="14"><path d="M0 0 L13 12 L26 0 L20 0 L13 6 L6 0Z" fill="#ffe600"/></svg>

<div class="breadcrumb"><a href="#">Home</a> &gt; <span class="current">Promote Great Times</span></div>
<nav class="sub-nav"><span class="active">HOME</span><span>ABOUT US</span><span>TERMS &amp; CONDITION</span><span>PRIVACY POLICY</span><span>CONTACT US</span></nav>

<section class="hero" role="img" aria-label="Band playing a gig on a pebble beach with people dancing">
  <svg class="hero-arrows" width="56" height="34"><path d="M14 2 L2 17 L14 32" fill="none" stroke="#e60012" stroke-width="5"/><path d="M38 2 L50 17 L38 32" fill="none" stroke="#e60012" stroke-width="5"/></svg>
  <svg class="hero-down" width="56" height="70"><path d="M18 0 H38 V36 H54 L28 70 L2 36 H18Z" fill="#ffe600"/></svg>
  <div class="hero-title"><span class="big">SEA</span><span class="side">SIDE</span><span class="sub">EXPERIENCE</span></div>
  <p class="hero-caption">Lorem Ipsum is simply dummy text of the printing and typesetting industry. Lorem Ipsum has been the industry's standard dummy text ever since the 1500s, when an unknown printer took a galley of type and scrambled it to make a type specimen book. It has survived not only five centuries.</p>
</section>

<div class="thumbs">
  <div class="thumb band" role="img" aria-label="Beach gig"></div>
  <div class="thumb rock" role="img" aria-label="Rock climbing group"></div>
  <div class="thumb band" role="img" aria-label="Beach gig"></div>
  <div class="thumb forest" role="img" aria-label="Forest camping"></div>
  <div class="thumb rock" role="img" aria-label="Rock climbing group"></div>
  <div class="thumb band active" role="img" aria-label="Beach gig"></div>
  <div class="thumb forest" role="img" aria-label="Forest camping"></div>
</div>

<section class="intro">
  <h1><span>PROMOTE</span> GREAT TIMES</h1>
  <p>Lorem Ipsum is simply dummy text of the printing and typesetting industry. Lorem Ipsum has been the industry's standard dummy text ever since the 1500s, when an unknown printer took a galley of type and scrambled it to make a type specimen book. It has survived not only five centuries, but also the leap into electronic typesetting, remaining essentially unchanged. It was popularised in the 1960s with the release of Lettrane sheets containing Lorem Ipsum passages, and more recently with desktop publishing software like Alder PageForge including versions of Lorem Ipsum.</p>
</section>

<div class="promote-btn">PROMOTE</div>
<div class="social"><span class="rss"></span><span class="s2"></span><span class="s3"></span><span class="s4"></span></div>

<footer class="site-footer">
  <div class="footer-nav"><svg width="12" height="22" style="vertical-align:-4px;margin-right:10px"><path d="M1 1 L10 11 L1 21" fill="none" stroke="#e60012" stroke-width="3"/></svg>FIND GREAT TIMES • <span class="active">PROMOTE GREAT TIMES</span> • SHARE GREAT TIMES</div>
  <div class="footer-legal"><b>TERMS &amp; CONDITION &nbsp;|&nbsp; PRIVACY POLICY</b><br><small>Copyright 2011. GOODDAYSOUT.NET. All Rights Reserved</small></div>
</footer>
</body>
</html>
```